Webdesign für Ingenieurbüro
Zielgruppe
Ingenieurbüro Varnotek GmbH
Leistungen:
Siedlungswasserwirtschaft
Straßen- und Ingenieurbau
Hochwasserschutz / Wasserbau
Pegelanlagen
Komplexerschließungen
Koordinierung nach BaustellV
Landschaftsbau
Zielgruppe ist die Öffentliche Hand
Aufgabenstellung
Leistungsbereiche und Stellenangebote (zZt. 3 Stück) sollen zu gleichen Teilen im Fokus stehen. Call to action zum Berweberformular ist nötig.
Zu beachten wäre, dass das Unternehmen für öffentliche Auftraggeber arbeitet. Die Seite sollte klar strukturiert und seriös wirken.
Der Login-Bereich soll in den Hintergrund treten, eventuell über dem footer.
Logo aus dem Cover - siehe anbei übernehmen

```html
<!DOCTYPE html>
<html lang="de">
<head>
<meta charset="utf-8">
<title>Ingenieurbüro Varnotek GmbH</title>
<link href="https://fonts.googleapis.com/css2?family=Roboto:wght@400;500;700&display=swap" rel="stylesheet">
<style>
  :root {
    --navy: #0b2e78;
    --blue: #009fe3;
    --ink: #1a1a1a;
    --white: #ffffff;
    --line: #c9d6ea;
  }
  * { box-sizing: border-box; margin: 0; padding: 0; }
  html, body { width: 819px; height: 1200px; overflow: hidden; background: var(--white); }
  body { position: relative; font-family: "Roboto", Arial, sans-serif; color: var(--navy); }

  .site-header { position: absolute; left: 0; top: 0; width: 819px; height: 88px; background: var(--white); }
  .brand { position: absolute; left: 110px; top: 32px; display: flex; align-items: center; gap: 6px; font-size: 11px; line-height: 12px; font-weight: 500; color: var(--navy); }
  .brand-mark { width: 12px; height: 12px; background: var(--navy); flex: none; }
  .main-nav { position: absolute; left: 237px; top: 43px; display: flex; gap: 16px; font-size: 11.5px; font-weight: 500; white-space: nowrap; }
  .main-nav a { color: var(--navy); text-decoration: none; }
  .main-nav a.active { color: var(--blue); }

  .hero { position: absolute; left: 0; top: 88px; width: 819px; height: 369px; }
  .hero-photo { position: absolute; inset: 0; background: linear-gradient(100deg, #5d6670 0%, #7f8890 35%, #9aa1a8 55%, #3e4f73 78%, #69717a 100%); }
  .hero-title { position: absolute; left: 85px; top: 66px; font-size: 30px; line-height: 32.5px; font-weight: 700; color: var(--white); }
  .hero-cta { position: absolute; left: 85px; top: 195px; width: 208px; height: 34px; background: var(--blue); color: var(--white); font-size: 17.5px; display: flex; align-items: center; justify-content: center; }

  .services { position: absolute; left: 85px; top: 367px; width: 648px; height: 74px; background: var(--white); }
  .service { position: absolute; top: 0; height: 74px; display: flex; flex-direction: column; align-items: center; justify-content: center; gap: 6px; font-size: 9.5px; font-weight: 500; color: var(--navy); white-space: nowrap; }
  .service svg { width: 18px; height: 20px; }
  .divider { position: absolute; top: 11px; width: 1px; height: 52px; background: var(--line); }

  .welcome-text { position: absolute; left: 85px; top: 542px; width: 290px; }
  .welcome-title { font-size: 15.5px; font-weight: 700; color: var(--blue); }
  .welcome-sub { margin-top: 6px; font-size: 11px; line-height: 13px; font-weight: 500; white-space: nowrap; }
  .welcome-body { margin-top: 7px; font-size: 8.3px; line-height: 12.8px; color: var(--ink); white-space: nowrap; }
  .accent-bar { position: absolute; left: 628px; top: 492px; width: 105px; height: 18px; background: var(--navy); }
  .accent-frame { position: absolute; left: 391px; top: 696px; width: 160px; height: 72px; border: 1px solid var(--navy); }
  .office-photo { position: absolute; left: 416px; top: 510px; width: 317px; height: 238px; background: linear-gradient(180deg, #d9dde3 0%, #c7d2e2 45%, #b9bfc8 75%, #e4dcdc 100%); box-shadow: 0 6px 14px rgba(11,46,120,.15); }

  .assoc-title { position: absolute; left: 0; top: 814px; width: 813px; text-align: center; font-size: 16.5px; font-weight: 700; }
  .assoc-grid { position: absolute; left: 128px; top: 862px; width: 562px; height: 222px; display: grid; grid-template-columns: repeat(4, 1fr); grid-template-rows: repeat(2, 1fr); box-shadow: 0 8px 18px rgba(11,46,120,.12); }
  .cell { display: flex; align-items: center; justify-content: center; text-align: center; padding: 0 12px; font-size: 11px; line-height: 12.8px; font-weight: 500; }
  .cell.dark { background: var(--navy); color: var(--white); }
  .cell.light { background: var(--white); color: var(--navy); }
  .cell.photo-workers { background: linear-gradient(135deg, #3d4550, #8a7e70 50%, #5a5f66); }
  .cell.photo-site { background: linear-gradient(180deg, #e6e4e0, #c8b9a2 60%, #b8a68a); }
  .cell.photo-plant { background: linear-gradient(180deg, #d4dbe3, #9fb0c0 45%, #4f7593); }

  .site-footer { position: absolute; left: 0; top: 1122px; width: 819px; height: 78px; background: var(--navy); color: var(--white); }
  .footer-brand { position: absolute; left: 85px; top: 30px; font-size: 10.5px; line-height: 10.5px; font-weight: 500; }
  .footer-nav { position: absolute; left: 330px; top: 35px; display: flex; gap: 20px; font-size: 9px; }
  .footer-nav a { color: var(--white); text-decoration: none; }
  .footer-note { position: absolute; left: 0; top: 61px; width: 819px; text-align: center; font-size: 8.5px; color: #8ea3cc; }
</style>
</head>
<body>
  <header class="site-header">
    <div class="brand"><span class="brand-mark"></span><span>Ingenieurbüro<br>Varnotek GmbH</span></div>
    <nav class="main-nav">
      <a class="active" href="#">Stellenangebote</a>
      <a href="#">Leistungen</a>
      <a href="#">Unternehmen</a>
      <a href="#">Projekte</a>
      <a href="#">Kontakt</a>
      <a href="#">Impressum/Datenschutz</a>
    </nav>
  </header>

  <section class="hero">
    <div class="hero-photo" role="img" aria-label="Ingenieur mit weißem Schutzhelm in einer Werkhalle"></div>
    <h1 class="hero-title">Hinter erfolgreichen<br>Projekten steht ein<br>guter VARNOTEKer!</h1>
    <a class="hero-cta">Kontaktieren</a>
  </section>

  <div class="services">
    <div class="service" style="left:62px;width:126px">
      <svg viewBox="0 0 18 20" fill="none" stroke="#0b2e78" stroke-width="1"><path d="M9 1C6 6 3 9 3 13a6 6 0 0 0 12 0c0-4-3-7-6-12z"/><path d="M6 13a3 3 0 0 0 3 3"/></svg>
      Siedlungswasserwirtschaft</div>
    <div class="divider" style="left:187px"></div>
    <div class="service" style="left:188px;width:126px">
      <svg viewBox="0 0 18 20" fill="none" stroke="#0b2e78" stroke-width="1"><path d="M6 1L1 19M12 1l5 18M9 2v3M9 8v3M9 14v3"/></svg>
      Straßen- und Ingenieurbau</div>
    <div class="divider" style="left:313px"></div>
    <div class="service" style="left:314px;width:82px">
      <svg viewBox="0 0 18 20" fill="none" stroke="#0b2e78" stroke-width="1"><path d="M9 19V9M9 9C9 5 6 3 2 3c0 4 3 6 7 6zM9 9c0-4 3-6 7-6 0 4-3 6-7 6z"/></svg>
      Landschaftsbau</div>
    <div class="divider" style="left:396px"></div>
    <div class="service" style="left:397px;width:120px">
      <svg viewBox="0 0 18 20" fill="none" stroke="#0b2e78" stroke-width="1"><path d="M2 3h6v3H2zM8 4h4v6h3M5 6v6h7M2 15c2 1 3 1 5 0s3-1 5 0 3 1 5 0M2 18c2 1 3 1 5 0s3-1 5 0 3 1 5 0"/></svg>
      Kanalsanierungsberatung</div>
    <div class="divider" style="left:517px"></div>
    <div class="service" style="left:518px;width:96px">
      <svg viewBox="0 0 18 20" fill="none" stroke="#0b2e78" stroke-width="1"><path d="M9 1C6 6 3 9 3 13a6 6 0 0 0 12 0c0-4-3-7-6-12z"/><path d="M10 8l-3 5h3l-2 4"/></svg>
      Wasserbau</div>
  </div>

  <section>
    <div class="accent-bar"></div>
    <div class="accent-frame"></div>
    <div class="office-photo" role="img" aria-label="Bürogebäude des Ingenieurbüros mit Parkplatz"></div>
    <div class="welcome-text">
      <h2 class="welcome-title">Herzlich willkommen</h2>
      <p class="welcome-sub">Über 25 Jahre Ingenieurbüro VARNOTEK GmbH<br>Ingenieurleistungen aus Mittelstadt-Eichenau seit 1991</p>
      <p class="welcome-body">Willkommen bei der Ingenieurbüro VARNOTEK GmbH, einem<br>mittelständischen Unternehmen, welches 1991 gegründet wurde.<br>Wir sind ein zuverlässiger Partner für fachgerechte Beratung, Planung<br>und Bauüberwachung von Maßnahmen des Tief-, Wasser- und<br>Straßenbaues.<br>Hierfür sind 18 hochqualifizierte und engagierte Ingenieure und<br>technische Mitarbeiter verantwortlich. Modernste<br>Kommunikationstechnik und Spezialsoftware, sowie die Kreativität der<br>Mitarbeiter sind ein Garant für effektive Lösungen.</p>
    </div>
  </section>

  <section>
    <h2 class="assoc-title">In folgenden Verbänden arbeiten wir aktiv mit</h2>
    <div class="assoc-grid">
      <div class="cell photo-workers" role="img" aria-label="Zwei Ingenieure mit Laptop in einer Werkhalle"></div>
      <div class="cell dark">Ingenieurkammer<br>Elbland</div>
      <div class="cell photo-site" role="img" aria-label="Bagger und Muldenkipper auf einer Baustelle"></div>
      <div class="cell light">Vereinigung der Straßen- u. Verkehrsbauingenieure Elblands (VSVE), Bezirksgruppe Mittelstadt</div>
      <div class="cell light">Deutscher Verband für Wasserwesen, Abwasser und Abfall e. V. (DVWA-LV Elbland/Nord)</div>
      <div class="cell photo-plant" role="img" aria-label="Becken einer Kläranlage"></div>
      <div class="cell dark">Bund der Ingenieure für Wasserwesen, Umwelttechnik und Kulturbau (BIWU)</div>
      <div class="cell photo-site" role="img" aria-label="Bagger und Muldenkipper auf einer Baustelle"></div>
    </div>
  </section>

  <footer class="site-footer">
    <div class="footer-brand">Ingenieurbüro<br>Varnotek GmbH</div>
    <nav class="footer-nav"><a href="#">Impressum</a><a href="#">Datenschutz</a><a href="#">Kontakt</a></nav>
    <p class="footer-note">Lorem Ipsum</p>
  </footer>
</body>
</html>
```